Tessavale Communications

I need a very clean, uncomplicated design for an LA-based, very senior level strategic communications firm with about four associates. Landing page should stress LA, maybe a slider with downtown skyline, Malibu pier, and Rodeo Drive. In addition to landing page with firm's description, all else we'd need is services offered page and another for bios of associates.

Industry/Entity Type

Communications

Font styles to use
Sans Serif

```html
<!DOCTYPE html>
<html lang="en">
<head>
<meta charset="utf-8">
<title>Tessavale Communications</title>
<link rel="stylesheet" href="https://fonts.googleapis.com/css2?family=Open+Sans:wght@400;600&family=Questrial&display=swap">
<style>
:root{
  --brand:#135f97;
  --accent:#1b9ad6;
  --caption:rgba(32,160,220,.9);
  --text:#777;
  --heading:#333;
  --nav:#444;
  --btn-top:#2a6b9d;
  --btn-bottom:#0d3b61;
  --footer:#4b4a4c;
  --rule:#e2e2e2;
}
*{margin:0;padding:0;box-sizing:border-box}
html,body{width:985px;height:1200px;overflow:hidden;background:#fff}
body{position:relative;font-family:"Open Sans",sans-serif;color:var(--text)}
.abs{position:absolute}

.site-header{left:0;top:0;width:985px;height:82px;background:#fff}
.brand{left:126px;top:19px;width:190px;display:flex;align-items:center;gap:8px}
.brand-dot{width:46px;height:46px;flex:none;border-radius:50%;background:var(--brand)}
.brand-name{font-family:"Questrial",sans-serif;font-size:17px;color:var(--brand);line-height:18px}
.main-nav{left:434px;top:37px;display:flex;gap:25px;font-family:"Questrial",sans-serif;font-size:13px;color:var(--nav)}
.main-nav .active{color:var(--brand)}

.hero{left:0;top:82px;width:985px;height:426px;background:linear-gradient(180deg,#a9c9e6 0%,#cfdfee 30%,#8b8f97 55%,#9a8e84 80%,#6f7774 100%)}
.hero-caption{left:120px;top:234px;width:398px;height:130px;background:var(--caption);padding:26px 24px 0 24px;color:#fff}
.hero-kicker{font-family:"Questrial",sans-serif;font-size:18px;line-height:1}
.hero-title{font-family:"Questrial",sans-serif;font-size:24px;line-height:1;margin-top:9px}
.hero-text{font-size:8px;line-height:14px;margin-top:7px}
.hero-arrow{top:262px}

.feature{top:540px;width:240px}
.feature-img{width:232px;height:105px;margin-left:1px}
.feature h2{font-family:"Questrial",sans-serif;font-weight:400;font-size:17.5px;color:var(--accent);margin-top:10px;line-height:1}
.feature p{font-size:9px;line-height:14.5px;margin-top:6px}
.btn{display:inline-block;width:82px;height:23px;margin-top:10px;margin-left:-3px;background:linear-gradient(var(--btn-top),var(--btn-bottom));border-radius:2px;color:#fff;font-family:"Questrial",sans-serif;font-size:9px;text-align:center;line-height:23px}

.divider{left:64px;top:774px;width:857px;height:12px;background:radial-gradient(ellipse at center top,rgba(0,0,0,.05),rgba(0,0,0,0) 70%)}

.section-title{font-family:"Questrial",sans-serif;font-weight:400;font-size:22px;color:var(--heading);line-height:1}
.about{left:123px;top:818px;width:340px}
.about p{font-size:9.3px;line-height:16px;margin-top:12px}
.about p + p{margin-top:4px}
.about h3{font-size:10px;font-weight:600;color:var(--brand);margin-top:10px;margin-left:2px}
.offers{list-style:none;margin-top:6px;margin-left:4px}
.offers li{font-size:9.3px;line-height:19.5px;padding-left:7px;position:relative}
.offers li::before{content:"";position:absolute;left:0;top:7px;border-left:3px solid var(--brand);border-top:3px solid transparent;border-bottom:3px solid transparent}

.news{left:500px;top:818px;width:370px}
.news-lead{display:flex;gap:31px;margin-top:14px}
.news-img{width:134px;height:89px;flex:none;margin-left:2px;background:linear-gradient(135deg,#e8eef2,#bfc7cc 50%,#8d8a85)}
.news h4{font-family:"Questrial",sans-serif;font-weight:400;font-size:13px;color:#444;line-height:18px}
.news p{font-size:9px;line-height:14.5px;margin-top:4px}
.news a{font-size:9.5px;color:var(--accent);text-decoration:none;display:block;margin-top:4px}
.news-item{margin-top:12px;margin-left:2px}
.news-item + .news-item{border-top:1px solid var(--rule);padding-top:12px;margin-top:14px}

.site-footer{left:0;top:1108px;width:985px;height:92px;background:var(--footer)}
.foot-nav{left:125px;top:25px;font-family:"Questrial",sans-serif;font-size:13px;color:#fff;word-spacing:2px}
.foot-nav span{margin:0 6px;}
.copyright{left:125px;top:48px;font-size:9px;color:#aaa}
.social{left:762px;top:21px;display:flex;gap:3px}
.social i{width:22px;height:22px;border-radius:50%;background:#e8e8e8;display:block}
</style>
</head>
<body>

<header class="site-header abs">
  <div class="brand abs"><span class="brand-dot"></span><span class="brand-name">Tessavale<br>Communications</span></div>
  <nav class="main-nav abs">
    <span class="active">HOME</span><span>ABOUT US</span><span>SERVICES</span><span>ASSOCIATES</span><span>CONTACT US</span>
  </nav>
</header>

<section class="hero abs" role="img" aria-label="Photograph of the downtown Los Angeles skyline under a blue sky"></section>
<div class="hero-caption abs">
  <div class="hero-kicker">ETIAM EST VENENATIS TRISTIQUE</div>
  <div class="hero-title">STRATEGIC COMMUNICATIONS</div>
  <p class="hero-text">Mauris vel lacus vitae felis vestibulum volutpat Etiam est nunc venenatis in tristique eu imperdiet ac nisl Cum sociis natoque penatibus et magnis</p>
</div>
<svg class="hero-arrow abs" style="left:60px" width="24" height="58" viewBox="0 0 24 58"><polyline points="22,2 2,29 22,56" fill="none" stroke="#fff" stroke-width="1.5"/></svg>
<svg class="hero-arrow abs" style="left:901px" width="24" height="58" viewBox="0 0 24 58"><polyline points="2,2 22,29 2,56" fill="none" stroke="#fff" stroke-width="1.5"/></svg>

<article class="feature abs" style="left:128px">
  <div class="feature-img" role="img" aria-label="Photograph of a businessman touching a network diagram" style="background:linear-gradient(90deg,#5d5f62,#8a8d90 50%,#2b2e33)"></div>
  <h2>WHAT WE DO</h2>
  <p>Morbi eget arcu Morbi porta libero id ullamcorper nonummy nibh ligula pulvinar metus</p>
  <span class="btn">READ MORE</span>
</article>
<article class="feature abs" style="left:381px">
  <div class="feature-img" role="img" aria-label="Illustration of connected blue figures in a network" style="background:linear-gradient(135deg,#f4f8fb,#cfe2ef 50%,#f4f8fb);border:1px solid #ddd"></div>
  <h2>OUR SERVICES</h2>
  <p>Morbi eget arcu Morbi porta libero id ullamcorper nonummy nibh ligula pulvinar metus</p>
  <span class="btn">READ MORE</span>
</article>
<article class="feature abs" style="left:636px">
  <div class="feature-img" role="img" aria-label="Photograph of a businesswoman fitting puzzle pieces together" style="background:linear-gradient(90deg,#dbe9f3,#f1ede9 50%,#d7e6f1)"></div>
  <h2>ASSOCIATES</h2>
  <p>Morbi eget arcu Morbi porta libero id ullamcorper nonummy nibh ligula pulvinar metus</p>
  <span class="btn">READ MORE</span>
</article>

<div class="divider abs"></div>

<section class="about abs">
  <h2 class="section-title">About Our Company</h2>
  <p>Vivamus porttitor g purus nisi eleifend libero a tempus libero lectus feugiat felis Morbi diam mauris viverra in gravida eu mattis in ante Morbi eget arcu Morbi porta libero id ullamcorper nonummy nibh ligula pulvinar metus eget consectetuer augue nisi quis lacus</p>
  <p>Ut ac mi quis lacus mollis aliquam Curabitur iaculis tempus eros Curabitur vel mi sit amet magna malesuada ultrices</p>
  <h3>What We Offers:</h3>
  <ul class="offers">
    <li>Euismod in elit Fusce ultricies orci ac feugiat suscipit</li>
    <li>Leo massa sodales velit</li>
    <li>Scelerisque mi tortor at ipsum</li>
  </ul>
</section>

<section class="news abs">
  <h2 class="section-title">News &amp; Projects</h2>
  <div class="news-lead">
    <div class="news-img" role="img" aria-label="Photograph of two businessmen shaking hands"></div>
    <div>
      <h4>Donec scelerisque leo ac risus Praesent sit amet est</h4>
      <p>Morbi porta libero id ullamcorper nonummy nibh ligula pulvinar metus eget consectet</p>
      <a href="#">Learn More</a>
    </div>
  </div>
  <div class="news-item">
    <h4>Ut nisi erat fermentum</h4>
    <p>Morbi porta libero id ullamcorper nonummy nibh ligula pulvinar metus eget</p>
  </div>
  <div class="news-item">
    <h4>Curabitur vel mi sit amet</h4>
    <p>Morbi porta libero id ullamcorper nonummy nibh ligula pulvinar metus eget con</p>
  </div>
</section>

<footer class="site-footer abs">
  <div class="foot-nav abs">Home<span>|</span>About us<span>|</span>Services<span>|</span>Associates<span>|</span>Contact us</div>
  <div class="copyright abs">© 2014 Company Name&nbsp; All right reserved&nbsp; Term of Use</div>
  <div class="social abs"><i></i><i></i><i></i><i></i></div>
</footer>

</body>
</html>
```